ECサイトのブランドコンセプトページ、商品ページ、プロモーションページのデザインをおねがいします。HTMLコーディングは含みません。

基本的な掲載コンテンツに変更はありません。添付のワイヤーを基に、フラワーショップのスイーツ店らしいシンプルで上品なデザインを希望します。作成頂いたコンセプトページをベースに他のページも制作したいと考えているため、その点も考慮して下さい。ロゴは添付ファイルのものを利用ください。

・デバイスフォントはWin "小塚ゴシック"、Mac "ヒラギノゴシック"、色がアースカラー。
・ターゲットは、30代~50代。スイーツ、花などの贈り物の購入者や、女子会、ホームパーティーでの購入者を想定。
・配色、クリエイティブは、参考サイトを参照。
[参考サイト]
http://www.morvanette.jp/
http://www.tolvicane.co.jp/

サイトリリース時にデザインに手を加えることをご了承ください。

ご質問・ご確認事項ありましたら「この依頼に質問」からお願いします。
それではたくさんのご応募お待ちしております。
3ページ
アースカラー、ピンク、ホワイト、
選定後納品ファイルですが、レイヤー情報を保持した.ai,.psdのいずれかを納品いただきます。当方、Win版CS5。
情報が少なかったので追記致します。

商品ページは全ての商品に共通したデザイン・キャッチコピーをおねがいします。
商品ページのイメージは下記サイトを参考にお願いします。

http://www.zenkuro8.com/menu/premiumcheesetart/

プロモーションページは下記サイトのような特集を組んで商品ページに誘導するイメージです

http://www.dorimenasu.com/new.php?twn=327
たくさんのご提案ありがとうございました。

ただ今、選考中です。
今しばらくお待ちください。
選定にお時間をいただき申し訳ございません。
とても良い提案が多く、クライアントの方でも決めかねております。

現在、クライアントの方で当選候補者様を数名に絞っていただいてるのですが、クライアントから候補者様のデザインされたプロモーションページが見たいという要望がございまして、ご応募いただいたランサー様に大至急、プロモーションページのデザインをお願い致します。当選候補者様には個別で修正依頼として、お願いを致します。修正依頼のないランサー様には申し訳ございませんが、ご了承ください。

プロモーションページをご提案いただけた方の中から必ず当選者を選ばせて頂くことを確約致します。
ご対応いただいている皆様
要件急変、大変申し訳ございません。

クライアントの方でこんなイメージも見たい、あんなイメージも見たいと意見が二転三転しておりまして、あれもこれもと対応していただくわけにはいかないので、ナビの画像など無しで小さめのおしゃれなフォントにしていただくだけで構いません。
プロモーションのページについては下記参考サイトのような白背景にフォントと余白で魅せるデザインでお願いできないでしょうか?

レイアウトはワイヤーの通りで構いません。

参考:http://vetrune-online.com/

お手数おかけして申し訳ございませんが、何卒よろしくお願い致します。

急な変更にご対応いただいているランサー様。
ありがとうございます。

ご提案いただいた案は全て、クライアントに提示致します。
ご提案いただいた案の中から必ず当選者を確定することを約束致します。

当選者のランサー様には当選したデザイン案でのブランドコンセプトページ、
商品ページの修正をお願い致します。お手数ではございますが、何卒ご了承くださいますようよろしくお願い申し上げます。
急な変更にも関わらず、ご対応いただきましたランサーの皆様、ありがとうございます。

現在、ご提案いただいたプロモーションページのデザインをクライアントに提出し選定中でございます。

提出致しましたデザインの中から当選者様を選ばせて頂きます。

当選者様には、お手数ではございますが、当選デザインでの商品ページ、コンセプトページの修正をお願い致しますこと、ご了承くださいますようお願い申し上げます。
当選者様は決定しているのですが、まだ修整をお願いすることがございまして、当選の確定を控えさせていただいております。

ご提案を頂いたランサーの皆様がたには、当選の確定をお待たせしてしまっていることお詫び申し上げます。

シンプルな中にも品があり、クライアント様の受けもよく、度重なる修正のお願いにもご対応いただき、クライアント様のイメージに近づけることができました。ありがとうございます。

急な要件変更にも関わらず、ご対応いただきましたランサーの皆様、ありがとうございました。

```html
<!DOCTYPE html>
<html lang="ja">
<head>
<meta charset="utf-8">
<title>BLOOM PATISSERIE — Concept</title>
<link rel="stylesheet" href="https://fonts.googleapis.com/css2?family=Noto+Serif+JP:wght@400;600&family=Cormorant+Garamond:wght@400;600&family=Great+Vibes&display=swap">
<style>
:root{
  --ink:#2b2420;
  --ink-soft:#5a4d44;
  --cream:#efe5c6;
  --cream-deep:#e2d3a4;
  --rose:#c8283a;
  --rose-soft:#f1c5cc;
  --pink-pill:#f4b9c8;
  --line:#d9d2c8;
  --paper:#ffffff;
  --panel:#faf8f5;
  --black:#0c0c0c;
}
*{box-sizing:border-box;margin:0;padding:0}
html,body{width:1200px;height:2896px;overflow:hidden;background:var(--paper)}
body{position:relative;font-family:"Noto Serif JP",serif;color:var(--ink)}
.abs{position:absolute}

.info-strip{left:40px;top:560px;width:1120px;height:34px;background:var(--cream);display:flex;align-items:center;padding-left:12px;font-size:17px;font-weight:600;letter-spacing:1px}
.header{left:40px;top:594px;width:1120px;height:226px;background:var(--paper)}
.util-links{right:20px;top:6px;font-size:10px;color:var(--ink-soft);letter-spacing:1px}
.brand{left:60px;top:70px}
.brand-name{font-family:"Cormorant Garamond",serif;font-weight:400;font-size:52px;letter-spacing:4px;color:var(--ink);line-height:1;white-space:nowrap}
.brand-mark{display:inline-block;width:18px;height:18px;border-radius:50%;background:var(--rose);margin-left:10px;vertical-align:middle}
.header-photo{left:560px;top:26px;width:560px;height:200px;background:linear-gradient(90deg,#fff 0%,#f6e9e4 30%,#e9c9c6 60%,#f3e7e0 100%)}

.nav{left:40px;top:820px;width:1120px;height:60px;background:linear-gradient(#f3ebcf,var(--cream-deep));display:flex;align-items:center;padding:0 24px;font-family:"Cormorant Garamond",serif;font-size:19px;font-weight:600}
.nav a{color:var(--ink);text-decoration:none;margin-right:52px}
.nav .nav-login{margin-left:auto;margin-right:24px}
.nav .cart{background:var(--pink-pill);border-radius:20px;padding:4px 18px;margin-right:0}

.crumb{left:64px;top:896px;font-family:"Cormorant Garamond",serif;font-size:16px;color:var(--ink-soft)}

.sidebar{left:48px;top:940px;width:224px}
.side-head{height:90px;background:linear-gradient(90deg,#fff,#e9e4de);border:1px solid var(--line);font-family:"Cormorant Garamond",serif;font-size:34px;padding:14px 10px;border-left:6px solid var(--black)}
.side-item{height:96px;border:1px solid var(--line);border-top:none;position:relative;padding:26px 8px 0}
.side-item .thumb{position:absolute;right:0;top:0;width:120px;height:95px}
.side-item p{position:relative;font-size:11px;color:var(--ink-soft);font-family:"Cormorant Garamond",serif}
.side-item b{position:relative;display:block;font-weight:600;font-size:17px;color:var(--ink)}
.banner{width:224px;background:var(--black);color:#fff;display:flex;align-items:center;justify-content:center;font-family:"Cormorant Garamond",serif;font-size:26px}
.calendar{width:224px;border:1px solid #888;display:flex;align-items:center;justify-content:center;font-family:"Cormorant Garamond",serif;font-size:26px;background:var(--paper)}

.card{left:320px;width:752px;background:var(--paper);border:1px solid var(--line);box-shadow:0 2px 8px rgba(0,0,0,.12)}
.message{top:932px;height:800px}
.label-tag{left:30px;top:30px;font-size:19px;padding:2px 24px 2px 14px;border-bottom:1px solid var(--line)}
.label-tag .dot{display:inline-block;width:12px;height:12px;border-radius:50%;background:var(--rose);margin-left:8px}
.message-body{left:0;top:90px;width:752px;text-align:center;font-size:20px;line-height:30px;letter-spacing:1px}
.message-body .lead{font-size:38px}
.message-photo{left:40px;top:600px;width:220px;height:150px;background:linear-gradient(160deg,#a8c2d4,#7a8d6a 60%,#5c4f3d)}
.signature{left:300px;top:680px;font-family:"Great Vibes",cursive;font-size:40px;color:var(--ink);white-space:nowrap}
.sig-flower{left:620px;top:640px;width:60px;height:60px;border-radius:50%;background:radial-gradient(circle at 50% 50%,var(--rose) 0 22px,#8a1a24 30px)}

.material{top:1800px;height:800px;overflow:hidden;background:linear-gradient(180deg,#f7f1ee,#eadcd5 60%,#f3ece8)}
.material-head{left:0;top:20px;background:var(--black);color:#fff;font-size:22px;padding:8px 30px 8px 24px;letter-spacing:2px}
.photo-petals{left:500px;top:0;width:252px;height:150px;border-radius:0 0 0 140px;background:linear-gradient(135deg,#8e1a22,#c8283a 50%,#6b1418)}
.photo-roses{left:0;top:120px;width:180px;height:300px;border-radius:0 140px 140px 0;background:radial-gradient(circle at 40% 40%,#e23a46,#9e1622 70%)}
.photo-rose-big{left:540px;top:560px;width:212px;height:240px;border-radius:140px 0 0 0;background:radial-gradient(circle at 50% 60%,#d1283a,#7c1119 60%,#456b3a 90%)}
.material-text{left:200px;top:160px;width:420px;text-align:center;font-size:19px;line-height:30px}
.material-text .cap{font-size:40px}
.material-text p{margin-bottom:26px}

.footer{left:0;top:2730px;width:1200px;height:120px}
.footer-flower{top:20px;width:70px;height:60px;background:radial-gradient(circle,var(--rose) 0 16px,transparent 18px)}
.copyright{left:0;top:84px;width:1200px;text-align:center;font-size:10px;color:var(--ink-soft);font-family:"Cormorant Garamond",serif}
</style>
</head>
<body>

<div class="abs info-strip">店舗説明文、店舗説明文、店舗説明文、店舗説明文</div>

<header class="abs header">
  <div class="abs header-photo" role="img" aria-label="花とスイーツを並べた淡いピンクの写真"></div>
  <div class="abs util-links">ご利用ガイド｜お問い合わせ｜会員登録｜マイページ｜カート</div>
  <div class="abs brand">
    <div class="brand-name">BLOOM PATISSERIE<span class="brand-mark"></span></div>
  </div>
</header>

<nav class="abs nav">
  <a>HOME</a><a>Concept</a><a>Product</a><a>Promotion</a><a>Monitor</a><a>Column</a>
  <a class="nav-login">Login</a><a class="cart">Shopping Cart</a>
</nav>

<div class="abs crumb">Top &gt;</div>

<aside class="abs sidebar">
  <div class="side-head">Product</div>
  <div class="side-item"><div class="thumb" role="img" aria-label="ロールケーキの写真" style="background:linear-gradient(90deg,#fff,#f2d7d7)"></div><p>Roll cake</p><b>ロールケーキ</b></div>
  <div class="side-item"><div class="thumb" role="img" aria-label="チーズタルトの写真" style="background:linear-gradient(90deg,#fff,#e9d6b8)"></div><p>Cheese tart</p><b>チーズタルト</b></div>
  <div class="side-item"><div class="thumb" role="img" aria-label="スポンジムースの写真" style="background:linear-gradient(90deg,#fff,#ead2c8)"></div><p>Sponge mousse</p><b>ローズムース</b></div>
  <div class="side-item"><div class="thumb" role="img" aria-label="焼き菓子の写真" style="background:linear-gradient(90deg,#fff,#dcc7a8)"></div><p>Baked sweets</p><b>焼き菓子</b></div>
  <div class="side-item"><div class="thumb" role="img" aria-label="メレンゲ菓子の写真" style="background:linear-gradient(90deg,#fff,#e8e0e4)"></div><p>Meringue</p><b>メレンゲ</b></div>
</aside>

<div class="abs banner" style="left:48px;top:1532px;height:228px">banner</div>
<div class="abs banner" style="left:48px;top:1890px;height:210px">banner</div>
<div class="abs calendar" style="left:48px;top:2108px;height:212px">calender</div>
<div class="abs calendar" style="left:48px;top:2332px;height:212px">calender</div>

<section class="abs card message">
  <div class="abs label-tag">お客さまへ<span class="dot"></span></div>
  <div class="abs message-body">
    <span class="lead">私</span>たちは花のように、ギフトやウェディングなど、<br>
    さまざまなシーンで<br>
    感動の演出をお手伝いさせていただきました。<br>
    その中から更に「お花の魅力をお伝えしたい！」<br>
    「お客様の喜ぶサプライズをお届けしたい！」<br>
    という気持ちでお菓子作りを始めました。<br>
    そして BLOOM PATISSERIE を作りました。<br>
    ギフトとして受け取った方がハッと笑顔になっていただける！<br>
    お召し上がりいただいた方のところに<br>
    一輪のお花が咲くようにとの願いを込めて、<br>
    特別な日に特別な気持ちをお届けできる！<br>
    ところもカラダもキレイになる！<br>
    こんなことを願って心を込めて作りました。<br>
    一輪一輪いっしょうけんめい咲いてくれたお花に感謝して…<br>
    今後とも宜しくご愛顧下さいますようお願い申し上げます。
  </div>
  <div class="abs message-photo" role="img" aria-label="薔薇園で花を手入れする作業の写真"></div>
  <div class="abs signature">Bloom Patisserie</div>
  <div class="abs sig-flower" role="img" aria-label="赤い薔薇の小さな写真"></div>
</section>

<section class="abs card material">
  <div class="abs photo-petals" role="img" aria-label="摘み取った赤い薔薇の花びらの写真"></div>
  <div class="abs photo-roses" role="img" aria-label="赤い薔薇の花束の写真"></div>
  <div class="abs photo-rose-big" role="img" aria-label="大輪の赤い薔薇の写真"></div>
  <div class="abs material-head">素材へのこだわり</div>
  <div class="abs material-text">
    <p><span class="cap">奥</span>山霧薔薇園は、「忘れられない薔薇を作る」を合言葉に、島根で薔薇の無農薬栽培を手掛けてきました。BLOOM PATISSERIE の多くは、山霧薔薇園の薔薇を使用しています。</p>
    <p>香りのバラ「花音」は、独特な芳香性と深紅の色、花弁の肉厚さが特徴。10年の品種、栽培技術の研究開発を経て作り出した山霧薔薇園のオリジナルブランドローズです。</p>
    <p>薔薇は、日本でも古くからバラを観賞用以外に活用されています。江戸時代の外科医療書の中にも「ロウ薔薇ウ」…現代で言うローズウォーターを生成する方法。</p>
  </div>
</section>

<footer class="abs footer">
  <div class="abs footer-flower" style="left:330px" role="img" aria-label="薔薇の花の小さな写真"></div>
  <div class="abs footer-flower" style="left:820px;background:radial-gradient(ellipse,#5f8a4a 0 16px,transparent 18px)" role="img" aria-label="緑の葉の小さな写真"></div>
  <div class="abs copyright">Copyright © BLOOM PATISSERIE SHOP All Rights Reserved.</div>
</footer>

</body>
</html>
```